Etiketten-Design für familiengeführten Weinbaubetrieb
Zielgruppe
Wir sind ein Familiengeführter Weinbaubetrieb und vermarkten unseren Wein in 0,75l Flaschen sowie auch Säfte und Schnäpse.
Zur zeit Verkaufen wir unseren Wein an Gastro und Private Kunden auch teils über Messen
Aufgabenstellung
Das derzeitige Etikett ist recht schlicht gestaltet und das Logo besteht rein aus dem geschriebenen Namen Winzerhof Dolmeck. Es kann aber auch gerne nur mit dem Namen Dolmeck ohne Winzerhof gearbeitet werden! Mit dem einbringen einer neuen Generation in den Betrieb wollen wir das aussehen unserer Produkte erneuern. Dazu kann sich gerne mit dem Namen als 'Logo' in jeglicher Art gespielt werden. Wir füllen unsere Weine in 0,75l Bordeaux Flaschen. Die Form des Etikett ist kein K.O. Kriterium jedoch wurde ursprünglich ein rund um Etikett angedacht. Sollten die Designes sich auch anders realisieren lassen sind wir gerne offen für Ideen.

```html
<!DOCTYPE html>
<html lang="de">
<head>
<meta charset="utf-8">
<title>Winzerhof Dolmeck – Blauer Zweigelt Etikett</title>
<link rel="stylesheet" href="https://fonts.googleapis.com/css2?family=Montserrat:wght@300;400;500&display=swap">
<style>
  :root {
    --page-bg: #ffffff;
    --label-black: #0b0b0c;
    --label-graphite: #2a2a2c;
    --label-sheen: #8d8d90;
    --wine-red: #c8102e;
    --vintage-red: #b3132b;
    --text-white: #f4f4f4;
    --text-grey: #b9b9bb;
    --grape-gold: #8c8463;
    --tree-grey: #d8d8d8;
  }
  html, body {
    margin: 0;
    padding: 0;
    width: 1097px;
    height: 1200px;
    overflow: hidden;
    background: var(--page-bg);
  }
  .canvas {
    position: relative;
    width: 1097px;
    height: 1200px;
  }
  .wine-label {
    position: absolute;
    left: 278px;
    top: 65px;
    width: 540px;
    height: 1069px;
  }
  .label-text {
    font-family: "Montserrat", sans-serif;
    fill: var(--text-white);
    text-anchor: middle;
  }
  .brand-pre { font-size: 11px; font-weight: 300; letter-spacing: 1px; }
  .brand-name { font-size: 27px; font-weight: 300; letter-spacing: 1px; }
  .badge-name { font-size: 12px; font-weight: 300; letter-spacing: 0.5px; }
  .vintage { font-size: 9px; font-weight: 400; letter-spacing: 6px; fill: var(--vintage-red); }
  .variety { font-size: 14px; font-weight: 400; letter-spacing: 3px; }
  .style-note { font-size: 7.5px; font-weight: 300; letter-spacing: 2.5px; fill: var(--text-grey); }
  .region { font-size: 8px; font-weight: 300; letter-spacing: 3.4px; fill: var(--text-grey); }
  .region-dac { font-size: 4px; letter-spacing: 1px; }
</style>
</head>
<body>
<main class="canvas">
  <svg class="wine-label" viewBox="70 150 250 495" xmlns="http://www.w3.org/2000/svg" aria-label="Weinetikett Winzerhof Dolmeck Blauer Zweigelt 2021">
    <defs>
      <linearGradient id="label-sheen" x1="75" y1="0" x2="312" y2="0" gradientUnits="userSpaceOnUse">
        <stop offset="0" stop-color="var(--label-graphite)"/>
        <stop offset="0.14" stop-color="var(--label-sheen)"/>
        <stop offset="0.3" stop-color="var(--label-graphite)"/>
        <stop offset="0.5" stop-color="var(--label-black)"/>
        <stop offset="0.72" stop-color="var(--label-black)"/>
        <stop offset="0.9" stop-color="var(--label-graphite)"/>
        <stop offset="1" stop-color="#5a5a5c"/>
      </linearGradient>
      <radialGradient id="tree-tone" cx="0.5" cy="0.5" r="0.6">
        <stop offset="0" stop-color="var(--tree-grey)" stop-opacity="0.75"/>
        <stop offset="1" stop-color="var(--tree-grey)" stop-opacity="0.05"/>
      </radialGradient>
    </defs>

    <!-- label body -->
    <path class="label-body" fill="url(#label-sheen)"
      d="M75 205 Q75 197 83 197 L124 197 L193 302 L262 197 L304 197 Q312 197 312 205 L312 590 L197 639 Q193 641 189 639 L75 590 Z"/>

    <!-- red badge with brand name -->
    <path class="brand-badge" fill="var(--wine-red)"
      d="M140 153 L246 153 Q252 153 249 159 L197 264 Q193 270 189 264 L137 159 Q134 153 140 153 Z"/>
    <text class="label-text badge-name" x="193" y="186">Dolmeck</text>

    <!-- wordmark -->
    <text class="label-text brand-pre" x="180" y="332">Winzerhof</text>
    <text class="label-text brand-name" x="190" y="368">Dolmeck</text>
    <path class="brand-rule" d="M150 380 Q220 372 292 366" stroke="var(--text-white)" stroke-width="0.7" fill="none"/>

    <!-- vintage, grape mark area, variety -->
    <text class="label-text vintage" x="196" y="427">2021</text>
    <g class="grape-mark" role="img" aria-label="Kleines Traubensymbol">
      <rect x="183" y="431" width="20" height="10" rx="4" fill="var(--grape-gold)" opacity="0.85"/>
    </g>
    <text class="label-text variety" x="193" y="456">BLAUER</text>
    <text class="label-text variety" x="193" y="473">ZWEIGELT</text>
    <text class="label-text style-note" x="194" y="486">trocken</text>

    <!-- vine tree area -->
    <g class="vine-area" role="img" aria-label="Weiße Zeichnung eines Rebstocks">
      <ellipse cx="196" cy="552" rx="48" ry="24" fill="url(#tree-tone)"/>
    </g>

    <!-- region -->
    <text class="label-text region" x="193" y="608">WEINVIERTEL<tspan class="region-dac" dx="1">DAC</tspan></text>
  </svg>
</main>
</body>
</html>
```